BRIARWOOD LOUNGE FRIDAY MAY 3

Flyer design for bar/nightclub event. Trying to keep a general theme with their flyers (see below) but would like to add some neon or some pop to it.

TEXT:

Briarwood Bar & Lounge Presents

LANTERN NIGHTS
GRAND OPENING EVENT

PURE HOUSE MUSIC W/

VORTEX
MARCO TELLEN
BRANDT & DJ WOBNIX

21+
9PM-130AM
712 K AVENUE DAVIS CA

Target Market(s)

House/dance music crowd.

Industry/Entity Type

Night Club

Font styles to use
Sans Serif

Colors
9bcb3c
fbee3d
ffffff

Requirements
Must have
• Large DJ names
Nice to have
• General theme of the attached flyers. Neon colors that stick with the theme. Anything else that looks cool will be considered

```html
<!DOCTYPE html>
<html lang="en">
<head>
<meta charset="utf-8">
<title>Briarwood Bar &amp; Lounge — Lantern Nights Grand Opening</title>
<link rel="stylesheet" href="https://fonts.googleapis.com/css2?family=Oswald:wght@500;700&family=Roboto+Condensed:wght@700&family=Cinzel:wght@700&display=swap">
<style>
  :root {
    --brand-green: #9bcb3c;
    --neon-yellow: #fbee3d;
    --white: #ffffff;
    --ember-red: #8e1a0c;
    --ember-deep: #5a0d06;
    --bark: #2a1508;
    --forest: #3f5a2a;
    --haze: #d9d9a8;
    --outline: #4a1204;
  }
  html, body {
    margin: 0;
    padding: 0;
    width: 848px;
    height: 1200px;
    overflow: hidden;
    background: var(--ember-deep);
  }
  .flyer {
    position: relative;
    width: 848px;
    height: 1200px;
    overflow: hidden;
    font-family: "Oswald", sans-serif;
  }
  .scene {
    position: absolute;
    inset: 0;
    background:
      radial-gradient(ellipse 260px 300px at 50% 66%, rgba(255,170,40,0.85), rgba(230,90,20,0.55) 45%, rgba(0,0,0,0) 75%),
      linear-gradient(180deg, var(--haze) 0%, #8f9a55 10%, var(--forest) 24%, #6a5a22 40%, #a4471a 55%, #b0361a 68%, var(--ember-red) 82%, var(--ember-deep) 100%);
  }
  .text-line {
    position: absolute;
    left: 0;
    right: 0;
    margin: 0;
    text-align: center;
    white-space: nowrap;
    line-height: 1;
  }
  .venue-badge {
    position: absolute;
    left: 264px;
    top: 44px;
    width: 300px;
    height: 300px;
    border-radius: 50%;
    background: var(--white);
    border: 14px solid var(--brand-green);
    box-sizing: content-box;
    display: flex;
    align-items: center;
    justify-content: center;
  }
  .venue-name {
    font-family: "Cinzel", serif;
    font-weight: 700;
    font-size: 27px;
    line-height: 1.25;
    color: #2f5a36;
    text-align: center;
    letter-spacing: 2px;
  }
  .presents {
    top: 420px;
    font-family: "Roboto Condensed", sans-serif;
    font-weight: 700;
    font-size: 30px;
    color: var(--white);
    text-shadow: 0 0 3px #000, 1px 1px 0 #000, -1px -1px 0 #000;
  }
  .event-frame {
    position: absolute;
    left: 92px;
    top: 504px;
    width: 664px;
    height: 168px;
    box-sizing: border-box;
    border: 8px solid var(--brand-green);
    border-radius: 18px;
    box-shadow: 0 0 18px var(--brand-green), inset 0 0 18px rgba(155,203,60,0.7);
  }
  .event-title {
    top: 532px;
    font-family: "Roboto Condensed", sans-serif;
    font-weight: 700;
    font-size: 66px;
    color: var(--neon-yellow);
    text-shadow: 0 0 4px var(--outline), 2px 2px 0 var(--outline), 0 0 14px rgba(251,238,61,0.6);
  }
  .event-subtitle {
    top: 604px;
    font-family: "Roboto Condensed", sans-serif;
    font-weight: 700;
    font-size: 46px;
    color: var(--neon-yellow);
    text-shadow: 0 0 4px var(--outline), 2px 2px 0 var(--outline);
  }
  .genre {
    top: 706px;
    font-weight: 700;
    font-size: 62px;
    letter-spacing: 3px;
    color: var(--neon-yellow);
    text-shadow: 0 0 4px var(--outline), 3px 3px 0 var(--outline), 0 0 10px var(--white);
  }
  .with {
    top: 810px;
    font-weight: 700;
    font-size: 30px;
    color: var(--neon-yellow);
    text-shadow: 2px 2px 0 var(--outline);
  }
  .lineup {
    font-weight: 700;
    font-size: 54px;
    color: var(--neon-yellow);
    text-shadow: 0 0 4px var(--outline), 3px 3px 0 var(--outline);
  }
  .lineup-first { top: 852px; }
  .lineup-second { top: 928px; }
  .divider { padding: 0 12px; }
  .info-band {
    position: absolute;
    left: 0;
    top: 1006px;
    width: 848px;
    height: 142px;
    background: var(--brand-green);
  }
  .hours {
    top: 1020px;
    font-weight: 700;
    font-size: 38px;
    color: var(--bark);
  }
  .date {
    top: 1070px;
    font-weight: 700;
    font-size: 62px;
    color: #5a1a0c;
  }
  .address {
    top: 1158px;
    font-weight: 700;
    font-size: 28px;
    letter-spacing: 1px;
    color: var(--neon-yellow);
  }
</style>
</head>
<body>
  <main class="flyer">
    <div class="scene" role="img" aria-label="Photo of a pine forest at sunset with a glowing campfire burning in the foreground"></div>

    <div class="venue-badge">
      <span class="venue-name">BRIARWOOD<br>BAR &amp; LOUNGE</span>
    </div>

    <p class="text-line presents">Presents</p>

    <div class="event-frame"></div>
    <h1 class="text-line event-title">LANTERN NIGHTS</h1>
    <p class="text-line event-subtitle">GRAND OPENING EVENT</p>

    <p class="text-line genre">HOUSE MUSIC</p>
    <p class="text-line with">- w/ -</p>

    <p class="text-line lineup lineup-first">VORTEX &amp; FRIENDS<span class="divider">|</span>MARCO TELLEN</p>
    <p class="text-line lineup lineup-second">BRANDT<span class="divider">|</span>DJ WOBNIX</p>

    <div class="info-band"></div>
    <p class="text-line hours">9pm -130am &bull; 21+</p>
    <p class="text-line date">FRIDAY, MAY 3 2019</p>
    <p class="text-line address">712 K AVENUE DAVIS CA</p>
  </main>
</body>
</html>
```